Web site design for news feed - Quillmar Live

We need to design a webpage to promote our web scraping newsfeed (similar to pagewheel) the name of the business is "Quillmar Live" ( a subsidiary of our company Quillmar - see www.corvel-holdings.example for details, DO NOT BASE THAT WEBSITE ON YOUR DESIGN).

We are inspired by famous Economists, we are inspired by empirical data, accuracy, but importantly the site needs to portray our "new approach" to delivering functional and "boring" financial news flow (pagewheel)

Websites we like:

www.zolvo.example - love the graphics
www.pagewheel.example - love the functionality
http://www.marketdial.example/ - practical
http://www.wirepost.example/ - practical
http://www.quenbrix.example/en-us/default.aspx
www.ldg.example
http://www.harbortimes.example/
www.velto.example

Our logo is attached

We like black and white, artful, mabel tunn etc
Updates

Hi All, please bear in mind that this is a NEWS site (it will need space to post stories) - so whilst the visual aspect is really important, the functionally around the amount of stories we can post is important too.

think marketdial.example, www.pitcrest.example, www.ldg.example - but feel (creativity) is zolvo.example, pagewheel.example

thanks all for some great designs.

i will revert to those closest tomorrow.
in the meantime, please bear in mind that the vision of skylines and economists helps me get to the design immediately, it resonates better, it helps me visually decide. 
lastly, in terms of the news "spaces", i will need to have 6 "top stories" and then room for maybe 20 more headlines..the top stories will need a picture, the 20 others will not (just headline text).
Thanks everyone again

Industry/Entity Type

Financial

Font styles to use
Serif
Sans Serif

```html
<!DOCTYPE html>
<html lang="en">
<head>
<meta charset="utf-8">
<title>Quillmar Live — Mobile Layouts</title>
<link href="https://fonts.googleapis.com/css2?family=Arimo:wght@400;700&family=Roboto+Condensed:wght@400;700&family=Noto+Serif:ital@1&display=swap" rel="stylesheet">
<style>
  :root{
    --canvas:#c0c0c0;
    --panel:#efefef;
    --ink:#222222;
    --muted:#8a8a8a;
    --accent:#e8640c;
    --black:#111111;
    --rule:#bdbdbd;
    --white:#ffffff;
  }
  *{box-sizing:border-box;margin:0;padding:0}
  html,body{width:952px;height:1200px;overflow:hidden;background:var(--canvas)}
  body{font-family:"Arimo",Arial,sans-serif;color:var(--ink)}
  .stage{position:relative;width:1116px;height:1406px;transform:scale(0.853);transform-origin:0 0}
  .column{position:absolute;width:320px;background:var(--panel)}
  .col-home{left:44px;top:48px;height:1324px}
  .col-more{left:391px;top:48px;height:756px;padding:0 11px}
  .col-popular{left:737px;top:48px;height:1014px}

  .topbar{height:34px;background:var(--black);display:flex;align-items:center;padding:0 12px;gap:10px;color:var(--white);font-size:12px}
  .topbar .sq{width:14px;height:14px;background:var(--white);display:block}
  .topbar .links{margin-left:16px;display:flex;gap:18px;letter-spacing:.2px}
  .topbar svg{margin-left:auto}
  .brandbar{height:72px;background:var(--white);display:flex;align-items:center;padding:0 14px 0 18px;border-top:1px dashed #999}
  .brand{display:flex;align-items:center;gap:12px;font-size:25px;line-height:23px;color:#7d7d7d}
  .brand .mark{width:30px;height:30px;background:var(--accent)}
  .hamburger{margin-left:auto}

  .hero{position:relative;height:276px;background:linear-gradient(180deg,#cfcfcf 0%,#9a9a9a 55%,#4a4a4a 100%)}
  .hero .tag{position:absolute;left:41px;top:30px;height:29px;background:var(--black);color:var(--white);border:2px solid var(--white);outline:1px solid var(--black);padding:3px 10px;font:400 15px "Roboto Condensed",sans-serif;z-index:1}
  .hero .tag b{font-weight:700}
  .hero .card{position:absolute;left:40px;top:58px;width:238px;height:183px;background:rgba(225,225,225,.82);padding:16px 8px 0 18px}
  .hero .kicker{font-size:9px;letter-spacing:.3px}
  .hero h2{font:700 21px/25px "Roboto Condensed",sans-serif;margin:7px 0 9px}
  .hero p{font-size:12.5px;line-height:16.5px}
  .hero .more{color:var(--accent);font:400 10px "Roboto Condensed",sans-serif;white-space:nowrap}
  .hero .arrow{position:absolute;top:112px}

  .signup{background:var(--white);padding:10px 10px 0;height:80px}
  .signup .row{display:flex;align-items:center;height:28px;margin-bottom:8px}
  .signup .label{font:400 17px "Roboto Condensed",sans-serif;width:89px;color:#333}
  .signup .field{width:170px;height:27px;border:1px solid #ccc;font-size:10px;color:#aaa;padding:8px}
  .signup .go{width:31px;height:27px;background:var(--accent);color:var(--white);font:700 17px/27px "Roboto Condensed",sans-serif;text-align:center;margin-left:3px}
  .social-chip{font-size:9px;border:1px solid #ccc;padding:2px 5px;color:#3b5998;background:#f6f6f6}
  .likes{font-size:9px;color:#444;margin:0 14px 0 6px}

  h3.section{font-weight:400;font-size:18px;color:var(--accent);padding:14px 10px 6px}
  .story{list-style:none;padding:9px 0 8px 0;border-bottom:1px dashed var(--rule);margin:0 11px}
  .story h4{font-weight:400;font-size:16px;line-height:19px}
  .story time{display:block;font:italic 12px/18px "Noto Serif",Georgia,serif;color:var(--muted)}
  .stories{padding:0}
  .col-more .story{margin:0}
  .col-more .stories{padding-top:4px}

  .ad{margin:17px 10px 0;height:62px;background:#ecebe4;border:3px solid #d4d2c8;display:flex;align-items:center;justify-content:space-between;padding:0 12px;font-size:18px;letter-spacing:.3px;color:#444;white-space:nowrap}
  .ad .name{font-weight:700;font-size:19px;letter-spacing:0}

  .col-popular h3.section{padding:5px 10px 6px}
  .feature{margin:0 13px;padding-bottom:9px;border-bottom:1px dashed var(--rule)}
  .feature .photo{height:147px;margin-top:10px}
  .feature h4{font-weight:400;font-size:16px;line-height:19px;margin-top:15px;max-width:255px}
  .feature p{font-size:12px;line-height:18px;color:#666;max-width:280px}
  .popular-list .story{margin:0 13px;padding:10px 0 9px}

  .site-footer{position:absolute;left:0;right:0;bottom:0;height:267px;background:var(--black);color:var(--white)}
  .site-footer .top{display:flex;align-items:center;height:61px;padding:0 20px}
  .site-footer .brand{color:var(--white);font-size:18px;line-height:17px}
  .site-footer .brand .mark{width:22px;height:22px}
  .site-footer .icons{margin-left:auto;display:flex;gap:14px}
  .site-footer .icons span{width:16px;height:16px;background:var(--white);display:block}
  .site-footer nav a{display:block;height:30px;line-height:30px;text-align:center;border-top:1px solid #2e2e2e;font:700 14px "Roboto Condensed",sans-serif;color:var(--white);text-decoration:none;text-transform:uppercase}
  .site-footer nav{border-bottom:1px solid #2e2e2e}
  .legal{position:absolute;left:13px;right:12px;bottom:0;height:66px;background:var(--white);color:#555;font-size:10px;line-height:16px;text-align:center;padding-top:10px}
  .legal span{margin:0 4px}
</style>
</head>
<body>
<div class="stage">

  <section class="column col-home">
    <div class="topbar">
      <span class="sq"></span><span class="sq"></span>
      <div class="links"><span>REGISTER</span><span>SIGN IN</span></div>
      <svg width="20" height="20" viewBox="0 0 20 20"><circle cx="8" cy="8" r="6" fill="none" stroke="#fff" stroke-width="2.5"/><line x1="12.5" y1="12.5" x2="18.5" y2="18.5" stroke="#fff" stroke-width="3.5" stroke-linecap="round"/></svg>
    </div>
    <header class="brandbar">
      <div class="brand"><span class="mark"></span><span>Quillmar<br>Live</span></div>
      <svg class="hamburger" width="40" height="28" viewBox="0 0 40 28"><rect y="0" width="40" height="6" rx="3" fill="#111"/><rect y="11" width="40" height="6" rx="3" fill="#111"/><rect y="22" width="40" height="6" rx="3" fill="#111"/></svg>
    </header>
    <div class="hero" role="img" aria-label="Black and white city skyline seen from above">
      <div class="tag">top <b>STORIES</b></div>
      <div class="card">
        <div class="kicker">NEWS</div>
        <h2>Lorem ipsum dolor sit amet, consectetur</h2>
        <p>adipisicing elit, sed do eiusmod tempor incididunt ut labore et dolore magna aliqua. Ut enim ad minim veniam. <span class="more">Read more &nbsp;⟶</span></p>
      </div>
      <svg class="arrow" style="left:6px" width="14" height="50" viewBox="0 0 14 50"><polyline points="12,2 2,25 12,48" fill="none" stroke="#eee" stroke-width="2"/></svg>
      <svg class="arrow" style="right:6px" width="14" height="50" viewBox="0 0 14 50"><polyline points="2,2 12,25 2,48" fill="none" stroke="#eee" stroke-width="2"/></svg>
    </div>
    <div class="signup">
      <div class="row"><span class="label">SUBSCRIBE</span><span class="field">Enter your email address</span><span class="go">GO</span></div>
      <div class="row"><span class="label">FOLLOW US</span><span class="social-chip">Like</span><span class="likes">2k people like this.</span><span class="social-chip" style="color:#2a6fa8">Follow</span></div>
    </div>
    <h3 class="section">Headline</h3>
    <ul class="stories">
      <li class="story"><h4>Phasellus tempus quam qua tempor pretium quisque.</h4><time>2 hours ago</time></li>
      <li class="story"><h4>Etiam porttitor accumsan pellentesque sapien felis.</h4><time>2 hours ago</time></li>
      <li class="story"><h4>Vestibulum ut justo ut urna hendrerit gravida eu ac eros.</h4><time>2 hours ago</time></li>
      <li class="story"><h4>Phasellus tempus quam qua tempor pretium quisque.</h4><time>2 hours ago</time></li>
      <li class="story"><h4>Donec vitae neque at quam rhoncus hendrerit.</h4><time>2 hours ago</time></li>
      <li class="story"><h4>Phasellus tempus quam qua tempor pretium quisque.</h4><time>2 hours ago</time></li>
      <li class="story"><h4>Etiam porttitor accumsan pellentesque sapien felis.</h4><time>2 hours ago</time></li>
      <li class="story"><h4>Vestibulum ut justo ut urna hendrerit gravida eu ac eros.</h4><time>2 hours ago</time></li>
      <li class="story"><h4>Phasellus tempus quam qua tempor pretium quisque.</h4><time>2 hours ago</time></li>
      <li class="story" style="border-bottom:none"><h4>Donec vitae neque at quam rhoncus hendrerit.</h4><time>2 hours ago</time></li>
    </ul>
    <div class="ad"><span>SLIM YOUR WALLET</span><span class="name">Trimfold</span></div>
  </section>

  <section class="column col-more">
    <ul class="stories">
      <li class="story"><h4>Phasellus tempus quam qua tempor pretium quisque.</h4><time>2 hours ago</time></li>
      <li class="story"><h4>Etiam porttitor accumsan pellentesque sapien felis.</h4><time>2 hours ago</time></li>
      <li class="story"><h4>Vestibulum ut justo ut urna hendrerit gravida eu ac eros.</h4><time>2 hours ago</time></li>
      <li class="story"><h4>Phasellus tempus quam qua tempor pretium quisque.</h4><time>2 hours ago</time></li>
      <li class="story"><h4>Donec vitae neque at quam rhoncus hendrerit.</h4><time>2 hours ago</time></li>
      <li class="story"><h4>Phasellus tempus quam qua tempor pretium quisque.</h4><time>2 hours ago</time></li>
      <li class="story"><h4>Etiam porttitor accumsan pellentesque sapien felis.</h4><time>2 hours ago</time></li>
      <li class="story"><h4>Vestibulum ut justo ut urna hendrerit gravida eu ac eros.</h4><time>2 hours ago</time></li>
      <li class="story"><h4>Phasellus tempus quam qua tempor pretium quisque.</h4><time>2 hours ago</time></li>
      <li class="story"><h4>Donec vitae neque at quam rhoncus hendrerit.</h4><time>2 hours ago</time></li>
    </ul>
  </section>

  <section class="column col-popular">
    <h3 class="section">Popular</h3>
    <article class="feature">
      <div class="photo" role="img" aria-label="Portrait photo of a man at an interview" style="background:linear-gradient(90deg,#b58f6c,#d9b08c 45%,#8a7a6a 85%,#6f5d4e)"></div>
      <h4>Phasellus tempus quam ut quam tempor pretium</h4>
      <p>Lorem ipsum dolor sit amet, consectetur adipiscing elit. Quisque felis enim.</p>
    </article>
    <article class="feature">
      <div class="photo" role="img" aria-label="Black and white photo of a man walking through an office" style="background:linear-gradient(90deg,#1a1a1a,#8c8c8c 35%,#e6e6e6 60%,#2a2a2a)"></div>
      <h4>Phasellus tempus quam ut quam tempor pretium</h4>
      <p>Lorem ipsum dolor sit amet, consectetur adipiscing elit. Quisque felis enim.</p>
    </article>
    <ul class="popular-list">
      <li class="story"><h4>Phasellus tempus quam qua tempor pretium quisque.</h4></li>
      <li class="story"><h4>Phasellus tempus quam qua tempor pretium quisque.</h4></li>
      <li class="story"><h4>Phasellus tempus quam qua tempor pretium quisque.</h4></li>
    </ul>
    <footer class="site-footer">
      <div class="top">
        <div class="brand"><span class="mark"></span><span>Quillmar<br>Live</span></div>
        <div class="icons"><span></span><span></span><span></span><span></span></div>
      </div>
      <nav>
        <a href="#">About Quillmar</a>
        <a href="#">Support &amp; Contact</a>
        <a href="#">Quillmar Live Network</a>
        <a href="#">Others</a>
      </nav>
      <div class="legal">
        ©2013 Quillmar Live. All Rights Reserved<br>
        <span>Trademarks</span><span>Terms of Service</span><br>
        <span>Privacy Policy</span><span>Jobs by Hirely</span>
      </div>
    </footer>
  </section>

</div>
</body>
</html>
```